Paws Of Kindness Business cards

Design a cool, modern business card for my bully breed rescue.

Contact Information for Business Card

Marlene
517-382-4061 Marlene@PawsOfKindnessRescue.net PawsOfKindnessRescue.net

Font styles to use
Serif
Sans Serif

Colors

Designer to choose colors to be used in the design.

Requirements
Must have
• logo and info. Color
Nice to have
• Foil. Maybe some paw prints on the back or some kind of dog illustration.

```html
<!DOCTYPE html>
<html lang="en">
<head>
<meta charset="utf-8">
<title>Paws Of Kindness Business Cards</title>
<link rel="stylesheet" href="https://fonts.googleapis.com/css2?family=Cinzel:wght@400;700&family=Lato:wght@400;900&display=swap">
<style>
  :root {
    --page: #ecebe8;
    --yellow: #ffc800;
    --black: #111111;
    --white: #ffffff;
    --red: #e0202a;
    --ink: #1a1a1a;
  }
  html, body {
    margin: 0;
    padding: 0;
    width: 1200px;
    height: 900px;
    overflow: hidden;
    background: var(--page);
  }
  .canvas {
    position: relative;
    width: 1200px;
    height: 900px;
    display: flex;
    flex-direction: column;
    align-items: center;
    justify-content: center;
    gap: 40px;
  }
  .card {
    position: relative;
    width: 700px;
    height: 400px;
    overflow: hidden;
    box-shadow: 0 2px 10px rgba(0,0,0,0.15);
  }
  .card-front {
    background: var(--yellow);
    display: flex;
    align-items: center;
    justify-content: center;
  }
  .brand {
    display: flex;
    align-items: center;
    gap: 14px;
    font-family: "Lato", sans-serif;
    font-weight: 900;
    color: var(--black);
    white-space: nowrap;
  }
  .brand-dot {
    border-radius: 50%;
    border: 3px solid var(--black);
    box-sizing: border-box;
  }
  .card-front .brand { font-size: 46px; }
  .card-front .brand-dot { width: 44px; height: 44px; }
  .card-back { background: var(--white); }
  .card-back .brand {
    position: absolute;
    top: 62px;
    right: 34px;
    font-size: 26px;
    gap: 10px;
  }
  .card-back .brand-dot { width: 26px; height: 26px; border-width: 2px; }
  .wave {
    position: absolute;
    inset: 0;
    width: 700px;
    height: 400px;
  }
  .holder-name {
    position: absolute;
    left: 70px;
    top: 144px;
    margin: 0;
    font-family: "Cinzel", serif;
    font-weight: 400;
    font-size: 28px;
    letter-spacing: 1px;
    color: var(--red);
  }
  .contact-list {
    position: absolute;
    left: 70px;
    top: 192px;
    margin: 0;
    padding: 0;
    list-style: none;
    font-family: "Lato", sans-serif;
    font-size: 17px;
    color: var(--ink);
    white-space: nowrap;
  }
  .contact-item {
    display: flex;
    align-items: center;
    gap: 8px;
    height: 25px;
  }
  .contact-icon { width: 15px; height: 15px; flex: none; }
</style>
</head>
<body>
<main class="canvas">
  <section class="card card-front" aria-label="Card front">
    <div class="brand"><span class="brand-dot"></span>Paws Of Kindness</div>
  </section>

  <section class="card card-back" aria-label="Card back">
    <svg class="wave" viewBox="0 0 700 400" aria-hidden="true">
      <path d="M0 322 C 180 340, 380 345, 520 300 C 600 275, 650 232, 700 212 L700 400 L0 400 Z" fill="var(--yellow)"/>
      <path d="M0 336 C 180 354, 380 359, 520 314 C 600 289, 650 246, 700 226 L700 400 L0 400 Z" fill="var(--white)"/>
      <path d="M0 343 C 180 361, 380 366, 520 321 C 600 296, 650 253, 700 233 L700 400 L0 400 Z" fill="var(--black)"/>
    </svg>

    <div class="brand"><span class="brand-dot"></span>Paws Of Kindness</div>

    <h1 class="holder-name">MARLENE</h1>
    <ul class="contact-list">
      <li class="contact-item">
        <svg class="contact-icon" viewBox="0 0 16 16" aria-hidden="true"><path d="M2 5 Q8 1 14 5 L12 7 L10 6 L6 6 L4 7 Z M3 9 H13 V14 H3 Z" fill="var(--red)"/></svg>
        517-382-4061
      </li>
      <li class="contact-item">
        <svg class="contact-icon" viewBox="0 0 16 16" aria-hidden="true"><rect x="1" y="3" width="14" height="10" fill="var(--red)"/><path d="M1 3 L8 9 L15 3" stroke="var(--white)" stroke-width="1.2" fill="none"/></svg>
        Marlene@PawsOfKindnessRescue.net PawsOfKindnessRescue.net
      </li>
      <li class="contact-item">
        <svg class="contact-icon" viewBox="0 0 16 16" aria-hidden="true"><circle cx="8" cy="8" r="7" fill="var(--red)"/><path d="M8 4 C6 4 5 5.5 5 7 C5 9 8 12 8 12 C8 12 11 9 11 7 C11 5.5 10 4 8 4 Z" fill="var(--white)"/></svg>
        www.PawsOfKindnessRescue.net PawsOfKindnessRescue.net
      </li>
    </ul>
  </section>
</main>
</body>
</html>
```